Acoustic Album Needs Cover Design

Bela Moravecz - Reflections: Quiet Harbor

The cover has five parts, each one has obligatory features:

The design in general could be that the person on the pictures is in white, empty space. Solve the shadows as you like, or use no shadows. Up to you.
The album is a happy, minimalistic, zen-like, acoustic album.

I. Main cover

Title: Reflections: Quiet Harbor
Artist: Bela Moravecz
Image “01 main cover”

II. Cover inside

Track list (12 songs) with durations
All songs written by Bela Moravecz
Copyright Velunotes 2016.
Image “02 cover inside”

III. Disc

Artist: Bela Moravecz
All songs written by Bela Moravecz (round on the edge)
Copyright Velunotes 2016. (round on the edge)
www.velunotes.example (round on the edge)

IV. Under the disc

No words, only some design feature. (Not one of the three images!)

V. Cover back

Track list (same as cover inside)
Copyright Velunotes 2016.
www.velunotes.example
Image “05 backside”
The paper of this page is longer than the main cover, because it is to be turned up when put in the CD case, and there is the spine with the name of the Artist and Title of the album. On both ends.

Important:
The main cover I need in RGB and also CMYK, all the others only CMYK.
I need the work file (cdr, ai or whatever you use)
I need the CMYK images prepared for printing (sizes set, and that little extra on the edges).
I need the RGB main cover cover in jpeg, 3000x3000 pixels.
That's all. :)

The most important of these all is of course the main cover RGB. Make this one first!

Here’s a sample to listen, it might inspire you:
https://files.sharebinex.example/u/48302716/Quiet%20Harbor%20medley%2020160118.mp3

If you take a closer look at my website, you can see the whole concept.

Good luck and enjoy!
Regards,
Bela

Target Market(s)

New Age spiritual people.

Requirements
Must have
• The three images:
• https://www.sharebinex.example/s/kq7rmzwpt3hbyfa/01%20main%20cover%2020160221.jpg?dl=0
• https://www.sharebinex.example/s/9pluvnexd4q2mrt/02%20cover%20inside%2020160221.jpg?dl=0
• https://www.sharebinex.example/s/tjb3oyhcw8kfz1d/05%20backside%2020160221.jpg?dl=0
• If there's a technical problem, let me know!

```html
<!DOCTYPE html>
<html lang="en">
<head>
<meta charset="utf-8">
<title>Bela Moravecz – Reflections: Quiet Harbor – Album Cover</title>
<link rel="stylesheet" href="https://fonts.googleapis.com/css2?family=Amatic+SC:wght@700&family=Courgette&display=swap">
<style>
  :root {
    --stage: #8f8f8f;
    --paper: #ffffff;
    --ink-light: #ffffff;
    --splash-pink: #f0509a;
    --splash-red: #ee3a33;
    --splash-orange: #f79a2a;
    --splash-yellow: #f7e14a;
    --splash-green: #7cc860;
    --splash-blue: #2f7fd6;
    --splash-violet: #b04fc8;
    --photo-top: #f4f6f9;
    --shirt-blue: #a9c6ea;
    --trouser-beige: #cbbfa8;
    --photo-floor: #f3f1ec;
    --title-shadow: rgba(0, 0, 0, 0.35);
  }

  html, body {
    margin: 0;
    padding: 0;
    width: 1200px;
    height: 849px;
    overflow: hidden;
    background: var(--stage);
  }

  .canvas {
    position: relative;
    width: 1200px;
    height: 849px;
  }

  .album-cover {
    position: absolute;
    left: 220px;
    top: 44px;
    width: 760px;
    height: 760px;
    overflow: hidden;
    background: var(--paper);
  }

  .splash-art {
    position: absolute;
    inset: 0;
    background:
      radial-gradient(circle at 8% 10%, var(--splash-pink) 0%, transparent 28%),
      radial-gradient(circle at 12% 40%, var(--splash-red) 0%, transparent 26%),
      radial-gradient(circle at 70% 8%, var(--splash-orange) 0%, transparent 25%),
      radial-gradient(circle at 92% 12%, var(--splash-pink) 0%, transparent 24%),
      radial-gradient(circle at 60% 40%, var(--splash-blue) 0%, transparent 20%),
      radial-gradient(circle at 82% 42%, var(--splash-green) 0%, transparent 22%),
      radial-gradient(circle at 74% 62%, var(--splash-yellow) 0%, transparent 24%),
      radial-gradient(circle at 90% 78%, var(--splash-red) 0%, transparent 26%),
      radial-gradient(circle at 85% 97%, var(--splash-violet) 0%, transparent 24%),
      linear-gradient(135deg, var(--splash-orange), var(--splash-pink));
  }

  .torn-paper {
    position: absolute;
    inset: 0;
    width: 760px;
    height: 760px;
  }

  .artist-name {
    position: absolute;
    left: 410px;
    top: 38px;
    width: 330px;
    margin: 0;
    font-family: "Amatic SC", cursive;
    font-weight: 700;
    font-size: 54px;
    line-height: 64px;
    letter-spacing: 3px;
    color: var(--ink-light);
    text-align: center;
    text-shadow: 0 1px 3px var(--title-shadow);
  }

  .album-title {
    position: absolute;
    left: 388px;
    top: 152px;
    width: 372px;
    margin: 0;
    font-family: "Courgette", cursive;
    font-weight: 400;
    font-size: 44px;
    line-height: 66px;
    color: var(--ink-light);
    text-shadow: 0 2px 4px var(--title-shadow);
  }

  .album-title span {
    display: block;
    white-space: nowrap;
  }

  .title-line-2 { padding-left: 106px; }
  .title-line-3 { padding-left: 160px; }
</style>
</head>
<body>
  <main class="canvas">
    <section class="album-cover" aria-label="Album front cover">
      <div class="splash-art" role="img" aria-label="Colourful watercolour paint splashes in pink, red, orange, yellow, green and blue"></div>

      <svg class="torn-paper" viewBox="0 0 760 760">
        <defs>
          <path id="torn-edge" d="M140 0 L400 0 L388 30 L404 58 L380 90 L396 120 L372 150 L378 190 L366 220 L392 250 L420 285 L446 320 L470 350 L492 392 L530 430 L548 470 L575 505 L590 548 L606 590 L600 630 L622 668 L616 710 L630 760 L0 760 L0 292 L18 268 L12 240 L40 214 L56 182 L48 150 L78 122 L96 92 L88 60 L118 34 L112 12 Z"/>
          <clipPath id="paper-clip">
            <use href="#torn-edge"/>
          </clipPath>
          <linearGradient id="photo-tone" x1="0" y1="0" x2="0" y2="1">
            <stop offset="0" stop-color="var(--photo-top)"/>
            <stop offset="0.3" stop-color="var(--shirt-blue)"/>
            <stop offset="0.62" stop-color="var(--shirt-blue)"/>
            <stop offset="0.8" stop-color="var(--trouser-beige)"/>
            <stop offset="1" stop-color="var(--photo-floor)"/>
          </linearGradient>
        </defs>
        <use href="#torn-edge" fill="var(--paper)"/>
        <g clip-path="url(#paper-clip)">
          <rect class="artist-photo" x="0" y="0" width="640" height="760" fill="url(#photo-tone)" role="img" aria-label="Photo of the artist in a light blue shirt and beige trousers, sitting cross-legged on white with an acoustic guitar"/>
          <use href="#torn-edge" fill="none" stroke="var(--paper)" stroke-width="28"/>
        </g>
      </svg>

      <h1 class="artist-name">Bela Moravecz</h1>
      <h2 class="album-title">
        <span class="title-line-1">Reflections:</span>
        <span class="title-line-2">Quiet</span>
        <span class="title-line-3">Harbor</span>
      </h2>
    </section>
  </main>
</body>
</html>
```